Carpet Cleaning Door Hanger Design Project

please design a door hanger for us. we do carpet cleaning. our company name is Velta Rug Works. our telephone number is 866-402-5719.

please make a special offer coupon.

please add bullets containing the following info-
Professional carpet, hardwood, tile & grout deep steam cleaning.
kid & pet safe.
fast drying.
100% eco friendly / toxin free products.
pet stain/s & odor control.
same day appointments.
clean uniformed employees.
and please put few other catchy lines.

please make a $20.00 of carpet cleaning coupon (restrictions apply).
please make a rooms starting at $59.99 (restrictions apply).

please also put- when you want the best for less call velta rug works.

Target Market(s)

home owners, home renters. new home buyers. new home sellers.

Industry/Entity Type

Home Improvement

Requirements
Must have
• special offer.
• double sided.
• must be a design for a door hanger.
Nice to have
• 100% satisfaction guaranteed bubble.
Should not have
• no website please

```html
<!DOCTYPE html>
<html lang="en">
<head>
<meta charset="utf-8">
<title>Velta Rug Works – Door Hanger</title>
<link href="https://fonts.googleapis.com/css2?family=Archivo+Black&family=Bebas+Neue&family=Open+Sans:wght@600;800&family=Roboto:ital,wght@1,900&display=swap" rel="stylesheet">
<style>
  :root {
    --navy: #2e3192;
    --red: #d6342b;
    --ribbon: #c7313b;
    --ribbon-dark: #8e1f27;
    --white: #ffffff;
    --ink: #1b1b1b;
    --backdrop: #a7a5a6;
    --photo-light: #e9e8e6;
    --photo-mid: #b9b5ae;
    --carpet: #9d968d;
    --gold: #e8b52a;
    --gold-dark: #b8861a;
    --seal-core: #2b2b2b;
  }
  * { margin: 0; padding: 0; box-sizing: border-box; }
  html, body { width: 1200px; height: 1200px; overflow: hidden; background: var(--backdrop); }
  .hanger {
    position: absolute; top: 70px; width: 411px; height: 1060px;
    background: var(--navy); overflow: hidden;
  }
  .hanger--front { left: 174px; }
  .hanger--back { left: 622px; }
  .hanger__art { position: absolute; inset: 0; }
  .abs { position: absolute; }
  .brand-name {
    position: absolute; left: 0; width: 100%; text-align: center;
    font-family: "Archivo Black", sans-serif; color: var(--white);
    font-size: 40px; line-height: 1; letter-spacing: 0.5px;
  }
  .ribbon {
    position: absolute; color: var(--white);
    font-family: "Open Sans", sans-serif; line-height: 1;
    display: flex; align-items: center; justify-content: center;
  }
  .ribbon--top { font-weight: 600; }
  .ribbon--bottom { font-weight: 800; }
  .features {
    position: absolute; left: 40px; top: 732px; list-style: none;
    font-family: "Roboto", sans-serif; font-style: italic; font-weight: 900;
    color: var(--white); font-size: 15px;
  }
  .features li { height: 26.3px; display: flex; align-items: center; gap: 8px; }
  .features svg { flex: none; }
  .call-strip {
    position: absolute; left: 0; top: 964px; width: 100%; height: 96px;
    background: var(--white); border-top: 6px solid var(--red); border-bottom: 6px solid var(--navy);
  }
  .call-strip__label {
    position: absolute; left: 110px; top: 22px;
    font-family: "Roboto", sans-serif; font-style: italic; font-weight: 900;
    color: var(--navy); font-size: 14px; letter-spacing: 0.5px;
  }
  .phone {
    font-family: "Roboto", sans-serif; font-style: italic; font-weight: 900;
    color: var(--red); line-height: 1;
  }
  .call-strip .phone { position: absolute; left: 20px; top: 40px; font-size: 32px; letter-spacing: 1px; }
  .coupon {
    position: absolute; left: 16px; top: 397px; width: 377px; height: 132px;
    background: var(--white); border: 2px dashed var(--navy);
    box-shadow: 0 4px 0 rgba(0,0,0,0.55);
  }
  .coupon__lead {
    position: absolute; left: 22px; top: 18px;
    font-family: "Bebas Neue", sans-serif; color: var(--navy); font-size: 38px; line-height: 1;
  }
  .coupon__value {
    position: absolute; left: 42px; top: 52px;
    font-family: "Bebas Neue", sans-serif; color: var(--red); font-size: 78px; line-height: 1;
  }
  .price {
    position: absolute; top: 548px; width: 184px; height: 138px;
    background: var(--white); box-shadow: 0 4px 0 rgba(0,0,0,0.55);
  }
  .price--carpet { left: 16px; }
  .price--rooms { left: 209px; }
  .price__head {
    height: 38px; background: var(--navy); color: var(--white);
    font-family: "Bebas Neue", sans-serif; font-size: 28px; line-height: 40px; text-align: center;
  }
  .price__from {
    position: absolute; left: 8px; top: 42px;
    font-family: "Bebas Neue", sans-serif; color: var(--red); font-size: 24px; line-height: 1;
  }
  .price__amount {
    position: absolute; left: 6px; right: 4px; bottom: 6px; white-space: nowrap;
    font-family: "Bebas Neue", sans-serif; color: var(--ink); font-size: 72px; line-height: 1;
  }
  .price__amount .currency { color: var(--navy); font-size: 50px; margin-right: 6px; }
  .tagline {
    position: absolute; left: 0; width: 100%; text-align: center;
    font-family: "Archivo Black", sans-serif; line-height: 1;
  }
  .tagline--red { color: var(--red); font-size: 26px; -webkit-text-stroke: 1px var(--white); }
  .tagline--blue { color: var(--navy); font-size: 38px; -webkit-text-stroke: 1px var(--white); }
  .back-rule { position: absolute; left: 27px; top: 1002px; width: 355px; height: 1px; background: var(--white); }
  .hanger--back .phone { position: absolute; left: 0; width: 100%; top: 1016px; text-align: center; font-size: 34px; letter-spacing: 1px; }
</style>
</head>
<body>

<!-- FRONT SIDE -->
<section class="hanger hanger--front">
  <svg class="hanger__art" width="411" height="1060" viewBox="0 0 411 1060">
    <defs>
      <linearGradient id="roomFront" x1="0" y1="0" x2="0" y2="1">
        <stop offset="0" stop-color="var(--photo-light)"/>
        <stop offset="0.45" stop-color="var(--photo-mid)"/>
        <stop offset="1" stop-color="var(--carpet)"/>
      </linearGradient>
      <radialGradient id="portrait" cx="0.5" cy="0.45" r="0.6">
        <stop offset="0" stop-color="#e9d6b8"/>
        <stop offset="1" stop-color="#cdbfae"/>
      </radialGradient>
      <radialGradient id="sealGold" cx="0.5" cy="0.4" r="0.6">
        <stop offset="0" stop-color="#f9dd6b"/>
        <stop offset="1" stop-color="var(--gold-dark)"/>
      </radialGradient>
    </defs>
    <rect x="0" y="280" width="411" height="440" fill="url(#roomFront)" role="img" aria-label="Photo: technician cleaning a living room carpet with a steam wand"/>
    <path d="M0,284 Q206,340 411,282 L411,300 Q230,365 0,310 Z" fill="var(--red)"/>
    <path d="M0,0 H411 V278 Q206,332 0,280 Z" fill="var(--navy)"/>
    <path d="M0,280 Q206,332 411,278" fill="none" stroke="var(--white)" stroke-width="4"/>
    <line x1="122" y1="0" x2="172" y2="52" stroke="var(--white)" stroke-width="2" stroke-dasharray="6 5"/>
    <circle cx="210" cy="97" r="60" fill="none" stroke="var(--white)" stroke-width="2" stroke-dasharray="6 5"/>
    <circle cx="330" cy="570" r="100" fill="var(--red)"/>
    <circle cx="334" cy="572" r="94" fill="url(#portrait)" role="img" aria-label="Photo: girl lying on a clean carpet beside her dog"/>
    <path d="M230,688 Q320,690 411,650 L411,690 Z" fill="var(--red)"/>
    <path d="M0,674 Q206,740 411,676 V1060 H0 Z" fill="var(--navy)"/>
    <path d="M0,674 Q206,740 411,676" fill="none" stroke="var(--white)" stroke-width="4"/>
    <!-- ribbons -->
    <path d="M202,353 H382 V388 H202 L214,370 Z" fill="var(--ribbon)"/>
    <path d="M215,388 L202,398 V388 Z" fill="var(--ribbon-dark)"/>
    <path d="M202,403 H382 L370,421 L382,439 H202 Z" fill="var(--ribbon)"/>
  </svg>

  <div class="brand-name" style="top:182px;">Velta Rug</div>
  <div class="brand-name" style="top:228px;">Works</div>

  <div class="ribbon ribbon--top" style="left:214px; top:353px; width:168px; height:35px; font-size:27px;">SPECIAL</div>
  <div class="ribbon ribbon--bottom" style="left:202px; top:403px; width:168px; height:36px; font-size:27px;">OFFER</div>

  <ul class="features">
    <li><svg width="13" height="13" viewBox="0 0 13 13"><circle cx="6.5" cy="6.5" r="5.5" fill="none" stroke="#fff" stroke-width="1.5"/><path d="M4,6.5 L6,8.5 L10,3.5" fill="none" stroke="var(--red)" stroke-width="1.8"/></svg>Professional Carpet, Hardwood</li>
    <li><svg width="13" height="13" viewBox="0 0 13 13"><circle cx="6.5" cy="6.5" r="5.5" fill="none" stroke="#fff" stroke-width="1.5"/><path d="M4,6.5 L6,8.5 L10,3.5" fill="none" stroke="var(--red)" stroke-width="1.8"/></svg>Tile &amp; Grout Deep Steam Cleaning.</li>
    <li><svg width="13" height="13" viewBox="0 0 13 13"><circle cx="6.5" cy="6.5" r="5.5" fill="none" stroke="#fff" stroke-width="1.5"/><path d="M4,6.5 L6,8.5 L10,3.5" fill="none" stroke="var(--red)" stroke-width="1.8"/></svg>Kid &amp; Pet Safe.</li>
    <li><svg width="13" height="13" viewBox="0 0 13 13"><circle cx="6.5" cy="6.5" r="5.5" fill="none" stroke="#fff" stroke-width="1.5"/><path d="M4,6.5 L6,8.5 L10,3.5" fill="none" stroke="var(--red)" stroke-width="1.8"/></svg>Fast Drying.</li>
    <li><svg width="13" height="13" viewBox="0 0 13 13"><circle cx="6.5" cy="6.5" r="5.5" fill="none" stroke="#fff" stroke-width="1.5"/><path d="M4,6.5 L6,8.5 L10,3.5" fill="none" stroke="var(--red)" stroke-width="1.8"/></svg>100% Eco Friendly / Toxin Free Products.</li>
    <li><svg width="13" height="13" viewBox="0 0 13 13"><circle cx="6.5" cy="6.5" r="5.5" fill="none" stroke="#fff" stroke-width="1.5"/><path d="M4,6.5 L6,8.5 L10,3.5" fill="none" stroke="var(--red)" stroke-width="1.8"/></svg>Pet Stand &amp; Odor Control.</li>
    <li><svg width="13" height="13" viewBox="0 0 13 13"><circle cx="6.5" cy="6.5" r="5.5" fill="none" stroke="#fff" stroke-width="1.5"/><path d="M4,6.5 L6,8.5 L10,3.5" fill="none" stroke="var(--red)" stroke-width="1.8"/></svg>Same Day Appointments.</li>
    <li><svg width="13" height="13" viewBox="0 0 13 13"><circle cx="6.5" cy="6.5" r="5.5" fill="none" stroke="#fff" stroke-width="1.5"/><path d="M4,6.5 L6,8.5 L10,3.5" fill="none" stroke="var(--red)" stroke-width="1.8"/></svg>Clean Uniformed Employees.</li>
  </ul>

  <div class="call-strip">
    <div class="call-strip__label">CALL US TODAY</div>
    <div class="phone">866-402-5719</div>
  </div>

  <svg class="abs" style="left:272px; top:920px;" width="136" height="136" viewBox="0 0 136 136" role="img" aria-label="Satisfaction guarantee seal">
    <circle cx="68" cy="68" r="66" fill="url(#sealGold)"/>
    <circle cx="68" cy="68" r="50" fill="var(--seal-core)"/>
    <circle cx="68" cy="68" r="30" fill="var(--gold)"/>
  </svg>
</section>

<!-- BACK SIDE -->
<section class="hanger hanger--back">
  <svg class="hanger__art" width="411" height="1060" viewBox="0 0 411 1060">
    <defs>
      <linearGradient id="roomBack" x1="0" y1="0" x2="0" y2="1">
        <stop offset="0" stop-color="var(--photo-light)"/>
        <stop offset="0.35" stop-color="var(--photo-mid)"/>
        <stop offset="0.5" stop-color="var(--carpet)"/>
        <stop offset="1" stop-color="#b3aea6"/>
      </linearGradient>
      <radialGradient id="sealGoldBack" cx="0.5" cy="0.4" r="0.6">
        <stop offset="0" stop-color="#f9dd6b"/>
        <stop offset="1" stop-color="var(--gold-dark)"/>
      </radialGradient>
    </defs>
    <rect x="0" y="160" width="411" height="760" fill="url(#roomBack)" role="img" aria-label="Photo: bright living room with sofa and freshly cleaned shaggy carpet"/>
    <path d="M0,182 Q150,235 330,212 Q200,255 0,230 Z" fill="var(--red)"/>
    <path d="M0,0 H411 V175 Q206,260 0,175 Z" fill="var(--navy)"/>
    <line x1="298" y1="0" x2="248" y2="52" stroke="var(--white)" stroke-width="2" stroke-dasharray="6 5"/>
    <circle cx="210" cy="97" r="60" fill="none" stroke="var(--white)" stroke-width="2" stroke-dasharray="6 5"/>
    <path d="M130,870 Q300,845 411,900 V920 Q300,870 130,870 Z" fill="var(--red)"/>
    <path d="M0,905 Q206,835 411,905 V1060 H0 Z" fill="var(--navy)"/>
    <path d="M0,905 Q206,835 411,905" fill="none" stroke="var(--white)" stroke-width="4"/>
    <circle cx="210" cy="305" r="66" fill="url(#sealGoldBack)"/>
    <circle cx="210" cy="305" r="50" fill="var(--seal-core)"/>
    <circle cx="210" cy="305" r="30" fill="var(--gold)"/>
  </svg>

  <div class="coupon">
    <div class="coupon__lead">SAVE UP TO</div>
    <div class="coupon__value">20%</div>
    <svg class="abs" style="left:186px; top:26px;" width="180" height="86" viewBox="0 0 180 86">
      <path d="M0,0 H176 V34 H0 L12,17 Z" fill="var(--ribbon)"/>
      <path d="M13,34 L0,44 V34 Z" fill="var(--ribbon-dark)"/>
      <path d="M0,52 H176 L164,68 L176,84 H0 Z" fill="var(--ribbon)"/>
    </svg>
    <div class="ribbon ribbon--top" style="left:198px; top:26px; width:164px; height:34px; font-size:26px;">SPECIAL</div>
    <div class="ribbon ribbon--bottom" style="left:186px; top:78px; width:164px; height:32px; font-size:26px;">OFFER</div>
  </div>

  <div class="price price--carpet">
    <div class="price__head">CARPET CLEANING</div>
    <div class="price__amount"><span class="currency">$</span>20.00</div>
  </div>
  <div class="price price--rooms">
    <div class="price__head">ROOMS CLEANING</div>
    <div class="price__from">FROM:</div>
    <div class="price__amount"><span class="currency">$</span>59.99</div>
  </div>

  <div class="tagline tagline--red" style="top:748px;">WHEN YOU WANT THE</div>
  <div class="tagline tagline--blue" style="top:774px;">BEST FOR LESS</div>
  <div class="tagline tagline--red" style="top:812px;">CALL</div>

  <div class="brand-name" style="top:898px;">Velta Rug</div>
  <div class="brand-name" style="top:944px;">Works</div>
  <div class="back-rule"></div>
  <div class="phone">866-402-5719</div>
</section>

</body>
</html>
```